K&R Security Services PTY. LTD.

Ive just had my logo made and I'm looking for some simple but strong designs for my business cards the company is a security company.

Please use dark colors.

Regards,

Owen Deloit

Reason: Need more time for discussion with other directors

Industry/Entity Type

Security

Font styles to use
Sans Serif
Decorative

```html
<!DOCTYPE html>
<html lang="en">
<head>
<meta charset="utf-8">
<title>K&amp;R Security Services – Business Cards</title>
<link rel="stylesheet" href="https://fonts.googleapis.com/css2?family=Open+Sans:wght@300;400;600&display=swap">
<style>
  :root {
    --backdrop: #1c1c1c;
    --card-light: #f4f4f4;
    --card-light-edge: #d9d9d9;
    --card-dark: #2e2e2e;
    --card-dark-glow: #4a4a4a;
    --ink-dark: #3a3a3a;
    --ink-muted: #6e6e6e;
    --ink-light: #d6d6d6;
    --ink-faint: #9a9a9a;
  }
  * { box-sizing: border-box; margin: 0; padding: 0; }
  html, body { width: 1200px; height: 900px; overflow: hidden; }
  body {
    background: var(--backdrop);
    font-family: "Open Sans", Arial, sans-serif;
    position: relative;
  }
  .card {
    position: absolute;
    width: 540px;
    height: 300px;
    border-radius: 2px;
  }
  .card--back {
    left: 110px;
    top: 110px;
    background: radial-gradient(ellipse at 45% 35%, #ffffff 0%, var(--card-light) 55%, var(--card-light-edge) 100%);
    color: var(--ink-dark);
  }
  .card--front {
    left: 550px;
    top: 490px;
    background: radial-gradient(ellipse at 50% 45%, var(--card-dark-glow) 0%, var(--card-dark) 60%, #232323 100%);
    color: var(--ink-light);
  }
  .brand {
    position: absolute;
    display: flex;
    align-items: center;
    gap: 10px;
    font-weight: 600;
    letter-spacing: 0.04em;
    white-space: nowrap;
  }
  .brand__mark {
    width: 14px;
    height: 14px;
    background: currentColor;
  }
  .card--back .brand {
    left: 150px;
    top: 92px;
    font-size: 24px;
    color: var(--ink-dark);
  }
  .card--front .brand {
    left: 0;
    right: 0;
    top: 110px;
    justify-content: center;
    font-size: 38px;
    color: var(--ink-light);
  }
  .holder {
    position: absolute;
    right: 36px;
    top: 40px;
    text-align: right;
  }
  .holder__name { font-size: 17px; font-weight: 400; color: var(--ink-dark); }
  .holder__role { font-size: 11px; font-weight: 300; color: var(--ink-muted); margin-bottom: 22px; }
  .holder__company,
  .holder__address { font-size: 11px; font-weight: 300; color: var(--ink-muted); line-height: 1.45; }
  .contact {
    position: absolute;
    left: 36px;
    bottom: 30px;
    list-style: none;
    font-size: 13px;
    font-weight: 400;
    line-height: 1.35;
    color: var(--ink-dark);
  }
  .contact__label { color: var(--ink-dark); }
  .contact__value { color: var(--ink-muted); font-weight: 300; }
  .website {
    position: absolute;
    left: 0;
    right: 0;
    bottom: 34px;
    text-align: center;
    font-size: 15px;
    font-weight: 300;
    color: var(--ink-faint);
    letter-spacing: 0.03em;
  }
</style>
</head>
<body>
  <section class="card card--back" aria-label="Business card, contact side">
    <div class="brand"><span class="brand__mark"></span>K&amp;R Security</div>
    <div class="holder">
      <p class="holder__name">Your Name</p>
      <p class="holder__role">president</p>
      <p class="holder__company">K&amp;R Security</p>
      <p class="holder__address">P.O. Box 12 Elmhurst<br>Victoria 3000</p>
    </div>
    <ul class="contact">
      <li><span class="contact__label">e-mail:</span> <span class="contact__value">owen@krsecvic.net.au</span></li>
      <li><span class="contact__label">business e-mail:</span> <span class="contact__value">office@krsecvic.net.au</span></li>
      <li><span class="contact__label">phone number:</span> <span class="contact__value">(03) 95550148</span></li>
      <li><span class="contact__label">mobile number:</span> <span class="contact__value">0400555193</span></li>
    </ul>
  </section>

  <section class="card card--front" aria-label="Business card, brand side">
    <div class="brand"><span class="brand__mark"></span>K&amp;R Security</div>
    <p class="website">www.yoursite.com</p>
  </section>
</body>
</html>
```